Brand new website for global research and investment startup

We need a simple website, maybe 3 pages: landing page with business description, investment philosophy, team and contact info.
We have a logo already that can be incorporated. Please use the logo only, not the text
We like the color green, something along the lines of #3D6C32 as the main color.
We'd like to design the website with geometric shapes in gradations of the base color. The shapes should suggest "work in progress", "built to last (a long time)", "solidity" and "indestructibility". One idea floating in my head sees smaller features with icosahedron and dodecahedron shapes, and maybe larger structures like crystal lattices; but please feel free to be creative and imagine your own.

```html
<!DOCTYPE html>
<html lang="en">
<head>
<meta charset="utf-8">
<title>Keystone Research &amp; Investment</title>
<link href="https://fonts.googleapis.com/css2?family=Arimo:wght@400;700&display=swap" rel="stylesheet">
<style>
:root{
  --green-main:#3d6c32;
  --green-dark:#2b5a32;
  --green-deep:#30562a;
  --green-bright:#6cc23a;
  --page-bg:#f3f5f2;
  --card-light:#e3eee0;
  --card-mid:#c5e1bd;
  --card-strong:#9bd190;
  --ink:#111;
  --ink-soft:#4a5a4a;
  --hero-text:#e6e8e4;
  --white:#fff;
}
*{margin:0;padding:0;box-sizing:border-box}
html,body{width:1200px;height:2224px;overflow:hidden}
body{font-family:"Arimo",Helvetica,Arial,sans-serif;background:var(--white);color:var(--ink);position:relative}
.site-header{position:absolute;top:0;left:0;width:1200px;height:66px;background:var(--green-main);z-index:2}
.brand{position:absolute;left:67px;top:18px;display:flex;align-items:center;gap:8px;color:var(--white);font-weight:700;font-size:22px;letter-spacing:1px}
.brand-square{width:14px;height:14px;background:var(--white)}
.main-nav{position:absolute;top:25px;left:0;width:1200px}
.main-nav a{position:absolute;color:var(--white);text-decoration:none;font-size:13px}
.main-nav a.active{text-decoration:underline}
.hero{position:absolute;top:66px;left:0;width:1200px;height:600px}
.hero-art{position:absolute;inset:0;background:
  linear-gradient(160deg,var(--green-deep) 0%,var(--green-main) 45%,#4f8f35 70%,var(--green-bright) 100%)}
.hero-title{position:absolute;left:68px;top:422px;color:var(--hero-text);font-weight:400;font-size:62px;line-height:78px;letter-spacing:-0.5px}
.who{position:absolute;top:666px;left:0;width:1200px;height:1110px;background:var(--page-bg)}
.who-title{position:absolute;left:67px;top:70px;font-size:45px;font-weight:400;color:var(--ink)}
.who-text{position:absolute;left:67px;top:150px;width:395px;font-size:19px;line-height:24px;color:var(--ink-soft)}
.beliefs-intro{position:absolute;left:597px;top:144px;width:500px;font-size:26px;line-height:33px;font-weight:400}
.belief{position:absolute;left:577px;width:544px;padding:35px 20px 0 20px}
.belief h3{font-size:26px;font-weight:400;padding-bottom:19px;border-bottom:1px solid var(--ink);margin-bottom:8px}
.belief p{font-size:13px;line-height:16.5px}
.belief-1{top:299px;height:176px;background:var(--card-light)}
.belief-2{top:528px;height:166px;background:var(--card-mid)}
.belief-3{top:786px;height:162px;background:var(--card-strong)}
.site-footer{position:absolute;top:1776px;left:0;width:1200px;height:448px}
.footer-brand{position:absolute;left:67px;top:68px;width:1064px;height:143px;border-top:1px solid var(--ink);border-bottom:1px solid var(--ink);display:flex;align-items:center;justify-content:center;gap:16px;color:var(--green-dark);font-weight:700;font-size:56px;letter-spacing:3px}
.footer-brand .brand-square{width:40px;height:40px;background:var(--green-dark)}
.footer-col{position:absolute;top:278px;font-size:13px;line-height:16.5px}
.footer-col a{display:block;color:var(--ink);text-decoration:none;margin-bottom:13.5px}
.col-address{left:67px}
.col-nav{left:454px}
.col-social{left:689px}
.col-legal{left:925px;width:200px}
.col-legal p{margin-bottom:13px}
</style>
</head>
<body>
<header class="site-header">
  <div class="brand"><span class="brand-square"></span>KEYSTONE</div>
  <nav class="main-nav">
    <a href="#" class="active" style="left:894px">Home</a>
    <a href="#" style="left:956px">About</a>
    <a href="#" style="left:1021px">Team</a>
    <a href="#" style="left:1086px">Contact</a>
  </nav>
</header>

<section class="hero">
  <div class="hero-art" role="img" aria-label="Layered green wave ribbons rising diagonally toward the upper right"></div>
  <h1 class="hero-title">Invest with founders<br>Invest in great companies</h1>
</section>

<section class="who">
  <h2 class="who-title">Who We Are</h2>
  <p class="who-text">We are a fundamental research and investment boutique dedicated to identifying, analysing and investing in founder-led public companies across the globe, as well as public companies which have preserved the entrepreneurial drive and management quality of their founding shareholders.</p>
  <p class="beliefs-intro">We follow a research and investment approach focused on three core beliefs</p>

  <article class="belief belief-1">
    <h3>Invest with Founders</h3>
    <p>Companies that deliver the most value for their customers often create the most value for their shareholders – a common attribute of founder driven businesses.</p>
  </article>
  <article class="belief belief-2">
    <h3>Invest in Great Companies</h3>
    <p>We focus on world-beating public companies, possessing lasting competitive advantages, with the conviction that over time, these companies will only grow stronger and deliver outstanding shareholder returns.</p>
  </article>
  <article class="belief belief-3">
    <h3>Invest in Undervalued Franchises</h3>
    <p>Our valuation methodology is focused on long-term organic revenue growth and earnings potential, combined with earnings visibility, profitability &amp; cash flow generation, capital repatriation and balance sheet strength.</p>
  </article>
</section>

<footer class="site-footer">
  <div class="footer-brand"><span class="brand-square"></span>KEYSTONE</div>
  <div class="footer-col col-address">
    Keystone Research &amp; Investment<br>anna@keystone-ri.com<br>6003 Lucerne<br>Switzerland
  </div>
  <div class="footer-col col-nav">
    <a href="#">Home</a><a href="#">About</a><a href="#">Team</a><a href="#">Contact</a>
  </div>
  <div class="footer-col col-social"><a href="#">Profile</a></div>
  <div class="footer-col col-legal">
    <p>© 2026 Keystone Research &amp; Investment.<br>All Rights Reserved.</p>
    <a href="#">Legal notice</a>
  </div>
</footer>
</body>
</html>
```